Elegant, High End Integrated Wellness Healthcare Practice

We need a brochure designed for an integrated mind-body wellness healthcare practice (www.larchveilclinic.com) . This brochure will be used when we cold call prospects (physicians to refer to our office, and potential consumers to utilize our services). Our practice is geographically located in the middle Tennessee USA region, although we have plans to become an international company as many of our offerings can be accessed anywhere in the world. Ultimately our goal is to have this brochure used as a leave-behind in an effort to introduce our integrated offerings to increase market share. The final product brochure should be both elegant and serious, with clean lines but also convey warmth and trust, as individuals who are coming for our services have usually struggled with their health for a significant amount of time before finding our practice.

The design brief was very specific about providing a high-end science-based 2-page brochure (not flier). Several designs submitted were fliers. The other designs were heavy on yoga or "woo woo" non-science-based looking pictures. This is a flier to appeal to physicians and other healthcare providers. Therefore the design must speak science and evidence-based methods of mind and body wellness care. I would also like to appeal to the other designers I paid extra for their submissions and who have indicated they will "respond in the coming days."

```html
<!DOCTYPE html>
<html lang="en">
<head>
<meta charset="utf-8">
<title>Larchveil Clinic – Brochure Cover</title>
<link href="https://fonts.googleapis.com/css2?family=Poppins:wght@400;500;600;700;800;900&display=swap" rel="stylesheet">
<style>
  :root {
    --page-bg: #e9e9ea;
    --forest-deep: #0b1f0c;
    --forest: #14361a;
    --olive-band: #2c3a17;
    --leaf: #71a940;
    --leaf-bright: #7cc24a;
    --white: #ffffff;
    --text-soft: #e6efe2;
  }
  * { box-sizing: border-box; margin: 0; padding: 0; }
  html, body {
    width: 1200px; height: 1200px; overflow: hidden;
    background: radial-gradient(ellipse at 50% 40%, #f6f6f7 0%, var(--page-bg) 70%);
    font-family: "Poppins", sans-serif;
  }
  .spread {
    position: absolute; left: 60px; top: 220px;
    width: 1080px; height: 760px;
    display: flex;
    box-shadow: 0 30px 60px rgba(0,0,0,.25);
  }
  .panel {
    position: relative; width: 540px; height: 760px; overflow: hidden;
    background: linear-gradient(160deg, var(--forest) 0%, var(--forest-deep) 60%, #081508 100%);
    color: var(--white);
  }

  /* back cover */
  .approach-title {
    position: absolute; left: 40px; top: 50px;
    font-weight: 800; font-size: 33px; letter-spacing: .5px; line-height: 1;
    white-space: nowrap;
  }
  .approach-rule {
    position: absolute; left: 40px; top: 98px; width: 380px; height: 3px;
    background: var(--leaf);
  }
  .brain-visual {
    position: absolute; left: 30px; top: 120px; width: 480px; height: 225px;
    background: radial-gradient(ellipse at 50% 45%, #3e7a2c 0%, #1d4a1c 40%, rgba(11,31,12,0) 75%);
  }
  .approach-copy {
    position: absolute; left: 40px; right: 40px; top: 360px;
    font-size: 12.5px; line-height: 1.5; text-align: center; color: var(--text-soft);
  }
  .cta-box {
    position: absolute; left: 80px; top: 510px; width: 330px;
    border: 2px solid var(--leaf); padding: 8px 0 6px; text-align: center;
  }
  .cta-label { color: var(--leaf-bright); font-weight: 800; font-size: 20px; line-height: 1.15; }
  .cta-phone { font-weight: 600; font-size: 18px; letter-spacing: 2px; line-height: 1.3; }

  .band-wave { position: absolute; left: 0; bottom: 0; width: 540px; height: 190px; }
  .web-link {
    position: absolute; left: 0; right: 0; bottom: 42px;
    display: flex; align-items: center; justify-content: center; gap: 10px;
    font-weight: 600; font-size: 24px; letter-spacing: 1.5px;
  }
  .web-icon { width: 26px; height: 26px; }

  /* front cover */
  .front-visual {
    position: absolute; left: 60px; top: 120px; width: 470px; height: 420px;
    background:
      radial-gradient(circle at 58% 30%, #c0392b 0%, #d35400 10%, rgba(211,84,0,0) 22%),
      radial-gradient(ellipse at 65% 50%, #4fa33a 0%, #2a6a24 40%, rgba(11,31,12,0) 78%);
  }
  .brand {
    position: absolute; left: 110px; top: 28px;
    display: flex; align-items: center; gap: 16px;
  }
  .brand-mark {
    width: 74px; height: 74px; border-radius: 50%;
    background: var(--white); border: 5px solid var(--leaf);
  }
  .brand-name {
    font-weight: 500; font-size: 30px; line-height: 1.15; letter-spacing: 1px;
    color: var(--white);
  }
  .headline {
    position: absolute; left: 90px; top: 330px;
    font-weight: 900; line-height: .95; color: var(--white);
    text-shadow: 0 2px 8px rgba(0,0,0,.4);
  }
  .headline .small { display: block; font-size: 40px; }
  .headline .large { display: block; font-size: 66px; }
</style>
</head>
<body>
<main class="spread">

  <section class="panel panel-back">
    <h2 class="approach-title">OUR UNIQUE APPROACH</h2>
    <div class="approach-rule"></div>
    <div class="brain-visual" role="img" aria-label="Glowing green brain hovering above an open hand"></div>
    <p class="approach-copy">At Larchveil Clinic we facilitate body and mind health and wellness through an integrated functional approach to care. This method of personalized care appreciates you as a unique individual with distinct health circumstances. We tailor our body and mind approaches to address your specific health concerns. The result is integrative healing-oriented care that addresses aspects of your whole person (body, mind, and spirit)</p>
    <div class="cta-box">
      <div class="cta-label">CALL FOR CONSULATION NOW</div>
      <div class="cta-phone">615-555-0148</div>
    </div>
    <svg class="band-wave" viewBox="0 0 540 190" preserveAspectRatio="none" aria-hidden="true">
      <path d="M0 125 C180 100 380 45 540 25 L540 190 L0 190 Z" fill="var(--olive-band)"/>
      <path d="M0 125 C180 100 380 45 540 25" fill="none" stroke="var(--white)" stroke-width="4"/>
    </svg>
    <div class="web-link">
      <svg class="web-icon" viewBox="0 0 26 26" aria-hidden="true">
        <circle cx="13" cy="13" r="12" fill="var(--white)"/>
        <g fill="none" stroke="var(--olive-band)" stroke-width="1.4">
          <circle cx="13" cy="13" r="7"/><ellipse cx="13" cy="13" rx="3" ry="7"/>
          <line x1="6" y1="13" x2="20" y2="13"/>
        </g>
      </svg>
      <span>larchveilclinic.com</span>
    </div>
  </section>

  <section class="panel panel-front">
    <div class="front-visual" role="img" aria-label="Green silhouette of a human head in profile with a heart-shaped bowl of fresh fruit and vegetables"></div>
    <div class="brand">
      <div class="brand-mark"></div>
      <div class="brand-name">Larchveil<br>Clinic</div>
    </div>
    <h1 class="headline">
      <span class="small">DISCOVER A BETTER</span>
      <span class="small">WAY TO</span>
      <span class="large">BETTER YOU</span>
    </h1>
    <svg class="band-wave" viewBox="0 0 540 190" preserveAspectRatio="none" aria-hidden="true">
      <path d="M0 25 C180 40 380 55 540 80 L540 190 L0 190 Z" fill="var(--leaf)"/>
      <path d="M0 25 C180 40 380 55 540 80" fill="none" stroke="var(--white)" stroke-width="4"/>
    </svg>
    <div class="web-link">
      <svg class="web-icon" viewBox="0 0 26 26" aria-hidden="true">
        <circle cx="13" cy="13" r="12" fill="var(--white)"/>
        <g fill="none" stroke="var(--leaf)" stroke-width="1.4">
          <circle cx="13" cy="13" r="7"/><ellipse cx="13" cy="13" rx="3" ry="7"/>
          <line x1="6" y1="13" x2="20" y2="13"/>
        </g>
      </svg>
      <span>larchveilclinic.com</span>
    </div>
  </section>

</main>
</body>
</html>
```